Birch Power and Wiring is a new company that specializes in solar pv. I need a card with similar attributes to the ones I have attached. I am after a two sided card with the logo on one side and the logo plus info on the other. I would prefer one side to be black and the other to be a colour but am open to suggestions. The colour scheme I was thinking of was blue or green. I plan on spot glossing the logos if that makes any difference. I have attached a file of my logo in a few colours, none of which I am completely sold on so please feel free to change colous to suit.
Thanks.
Calvin Birch, www.bpw.net.nz, calvin@bpw.net.nz, t. 0508 4 POWER m. 027463918

```html
<!DOCTYPE html>
<html lang="en">
<head>
<meta charset="utf-8">
<title>Birch Power and Wiring — Business Card and Letter Head</title>
<link rel="stylesheet" href="https://fonts.googleapis.com/css2?family=Jost:wght@300;400;500&display=swap">
<style>
  :root {
    --board: #dcdddf;
    --board-edge: #cfd0d2;
    --charcoal: #2a2a2a;
    --paper: #ffffff;
    --brand-green: #5cbf3a;
    --ink-light: #f2f2f2;
    --label-ink: #1e1e1e;
    --faint-mark: #8a8a8a;
    --shadow: 4px 6px 10px rgba(0, 0, 0, 0.35);
  }

  html, body {
    margin: 0;
    padding: 0;
    width: 1200px;
    height: 900px;
    overflow: hidden;
  }

  .board {
    position: relative;
    width: 1200px;
    height: 900px;
    background: radial-gradient(ellipse at 50% 40%, var(--board) 0%, var(--board-edge) 100%);
    font-family: "Jost", sans-serif;
  }

  .sheet {
    position: absolute;
    background: var(--charcoal);
    box-shadow: var(--shadow);
    overflow: hidden;
  }

  /* Business card — front */
  .card-front {
    left: 24px;
    top: 142px;
    width: 466px;
    height: 288px;
  }
  .card-front .logo-band {
    position: absolute;
    left: 0;
    top: 86px;
    width: 100%;
    height: 96px;
    background: var(--paper);
    display: flex;
    align-items: center;
    justify-content: center;
  }

  .brand-name {
    color: var(--brand-green);
    font-family: "Jost", sans-serif;
    font-weight: 500;
    white-space: nowrap;
    margin: 0;
    line-height: 1;
  }
  .card-front .brand-name { font-size: 31px; }

  /* Business card — back */
  .card-back {
    left: 24px;
    top: 470px;
    width: 466px;
    height: 287px;
  }
  .card-back .logo-strip {
    position: absolute;
    left: 0;
    top: 0;
    width: 97px;
    height: 100%;
    background: var(--paper);
  }
  .card-back .logo-strip .brand-name {
    position: absolute;
    left: 50%;
    top: 50%;
    font-size: 19px;
    transform: translate(-50%, -50%) rotate(-90deg);
  }

  .contact {
    position: absolute;
    left: 232px;
    top: 97px;
    color: var(--ink-light);
  }
  .contact-name {
    margin: 0 0 6px 26px;
    font-size: 17px;
    font-weight: 300;
    letter-spacing: 0.3px;
  }
  .contact-list {
    list-style: none;
    margin: 0;
    padding: 0;
  }
  .contact-list li {
    display: flex;
    align-items: center;
    height: 21px;
    font-size: 12px;
    font-weight: 300;
    letter-spacing: 0.3px;
  }
  .contact-list svg {
    width: 14px;
    height: 12px;
    margin-right: 10px;
    fill: none;
    stroke: var(--ink-light);
    stroke-width: 1.2;
  }
  .contact-list svg .solid { fill: var(--ink-light); stroke: none; }

  /* Letter head */
  .letterhead {
    left: 548px;
    top: 142px;
    width: 626px;
    height: 614px;
  }
  .letterhead .header {
    position: absolute;
    left: 0;
    top: 0;
    width: 100%;
    height: 130px;
    background: var(--paper);
    display: flex;
    align-items: center;
    justify-content: center;
  }
  .letterhead .header .brand-name { font-size: 44px; }
  .letterhead .footer-mark {
    position: absolute;
    right: 22px;
    bottom: 20px;
    color: var(--faint-mark);
    font-size: 15px;
    font-weight: 400;
    white-space: nowrap;
  }

  /* Presentation labels */
  .label {
    position: absolute;
    top: 790px;
    margin: 0;
    font-size: 29px;
    font-weight: 400;
    letter-spacing: 2.5px;
    color: var(--label-ink);
    text-align: center;
  }
  .label-card { left: 24px; width: 466px; }
  .label-letterhead { left: 548px; width: 626px; }
</style>
</head>
<body>
<main class="board">

  <section class="sheet card-front" aria-label="Business card front">
    <div class="logo-band">
      <p class="brand-name">Birch Power and Wiring</p>
    </div>
  </section>

  <section class="sheet card-back" aria-label="Business card back">
    <div class="logo-strip">
      <p class="brand-name">Birch Power and Wiring</p>
    </div>
    <div class="contact">
      <p class="contact-name">Calvin Birch</p>
      <ul class="contact-list">
        <li>
          <svg viewBox="0 0 14 12" aria-hidden="true">
            <circle cx="6" cy="6" r="4.8"/>
            <path d="M1.2 6h9.6M6 1.2c-2 2.6-2 7 0 9.6M6 1.2c2 2.6 2 7 0 9.6"/>
          </svg>
          www.bpw.net.nz
        </li>
        <li>
          <svg viewBox="0 0 14 12" aria-hidden="true">
            <path class="solid" d="M2 3h10v6.5H2z"/>
            <path d="M2 3l5 3.6L12 3" stroke="#2a2a2a"/>
          </svg>
          calvin@bpw.net.nz
        </li>
        <li>
          <svg viewBox="0 0 14 12" aria-hidden="true">
            <path class="solid" d="M1.5 4.5C1.5 2.5 4 2 7 2s5.5.5 5.5 2.5v1H10V4.2H4v1.3H1.5z"/>
            <path class="solid" d="M3.5 6.2h7l1 4H2.5z"/>
          </svg>
          0508 4 POWER
        </li>
        <li>
          <svg viewBox="0 0 14 12" aria-hidden="true">
            <rect class="solid" x="2" y="0.5" width="10" height="11" rx="2"/>
            <path d="M5.3 3.2c-.8.6-.6 2.6.9 4.2 1.4 1.4 2.6 1.5 3 1" stroke="#2a2a2a" stroke-width="1.4" stroke-linecap="round"/>
          </svg>
          027463918
        </li>
      </ul>
    </div>
  </section>

  <section class="sheet letterhead" aria-label="Letter head">
    <header class="header">
      <p class="brand-name">Birch Power and Wiring</p>
    </header>
    <p class="footer-mark">Birch Power and Wiring</p>
  </section>

  <h2 class="label label-card">Business Card</h2>
  <h2 class="label label-letterhead">Letter Head</h2>

</main>
</body>
</html>
```